A5 Personal trainer profile for brackmoor wellness

I need a A5 Landscape profile designed for the company I work for. Company name is Brackmoor Wellness. The profile is for personal trainers to let people know:

1. Brief description of themselves
2. Qualifications

A picture will be required on the right hand side of the profile. Brackmoor Wellness colours are green and white.

The Brackmoor Wellness Logo in the boarder of the example included must remain. We are looking for a clinical and professional design.

Industry/Entity Type

Health

```html
<!DOCTYPE html>
<html lang="en">
<head>
<meta charset="utf-8">
<title>Personal Trainer Profile – Brackmoor Wellness</title>
<link rel="stylesheet" href="https://fonts.googleapis.com/css2?family=Montserrat:wght@800;900&family=Source+Sans+3:wght@400;600&display=swap">
<style>
  :root {
    --backdrop-centre: #5a5a5a;
    --backdrop-edge: #050505;
    --green-bright: #52b848;
    --green-deep: #0b6a37;
    --green-band-dark: #0a5a2e;
    --green-band-mid: #0f7a3c;
    --photo-light: #b9e88a;
    --photo-mid: #8fd463;
    --photo-dark: #5aa83a;
    --ink: #4a4a4a;
    --white: #ffffff;
  }
  * { margin: 0; padding: 0; box-sizing: border-box; }
  html, body { width: 1200px; height: 999px; overflow: hidden; }
  body {
    position: relative;
    background: radial-gradient(ellipse 70% 70% at 50% 50%, var(--backdrop-centre), var(--backdrop-edge));
    font-family: "Source Sans 3", Arial, sans-serif;
  }
  .profile-card {
    position: absolute; left: 62px; top: 119px;
    width: 1076px; height: 761px;
    background: var(--white);
    overflow: hidden;
  }
  .portrait-area { position: absolute; left: 0; top: 0; width: 530px; height: 585px; }
  .title { position: absolute; left: 526px; font-family: "Montserrat", Arial, sans-serif; font-weight: 900; line-height: 1; white-space: nowrap; }
  .title-personal { top: 20px; font-size: 59px; color: var(--green-bright); letter-spacing: 0.5px; }
  .title-trainer { top: 76px; font-size: 104px; color: var(--green-deep); letter-spacing: -1px; }
  .title-name { top: 166px; font-size: 55px; color: var(--green-bright); }
  .section-heading {
    position: absolute; left: 530px;
    font-family: "Montserrat", Arial, sans-serif; font-weight: 800;
    font-size: 26.7px; color: var(--green-bright); white-space: nowrap;
  }
  .help-heading { top: 224px; }
  .help-list { position: absolute; left: 536px; top: 264px; list-style: none; }
  .help-list li {
    display: flex; align-items: center;
    font-size: 21.7px; color: var(--ink); line-height: 26px; white-space: nowrap;
  }
  .help-list svg { width: 18px; height: 12px; margin-right: 27px; flex: none; }
  .reviews-heading { top: 408px; }
  .testimonial {
    position: absolute; left: 527px; top: 450px; width: 512px;
    font-size: 21.7px; line-height: 26.5px; color: var(--ink);
  }
  .qualifications-band {
    position: absolute; left: 0; top: 585px; width: 1076px; height: 176px;
    background: linear-gradient(90deg, var(--green-band-dark) 0%, var(--green-band-mid) 42%, var(--green-bright) 100%);
    color: var(--white);
  }
  .qualifications-heading {
    position: absolute; left: 36px; top: 17px;
    font-family: "Montserrat", Arial, sans-serif; font-weight: 900; font-size: 25.7px;
  }
  .qualifications-list { position: absolute; left: 36px; top: 52px; list-style: none; }
  .qualifications-list li { font-size: 21.7px; line-height: 26px; position: relative; padding-left: 64px; white-space: nowrap; }
  .qualifications-list li::before { content: "•"; position: absolute; left: 0; font-size: 13px; }
  .brand-mark {
    position: absolute; left: 653px; top: 11px; width: 412px; height: 46px;
    background: var(--white);
    display: flex; align-items: center; gap: 10px; padding-left: 6px;
  }
  .brand-square { width: 30px; height: 30px; background: var(--green-band-mid); flex: none; }
  .brand-name {
    font-family: "Source Sans 3", Arial, sans-serif; font-weight: 600;
    font-size: 35px; color: var(--green-band-mid); white-space: nowrap; line-height: 1;
  }
</style>
</head>
<body>
  <main class="profile-card">
    <svg class="portrait-area" viewBox="0 0 530 585">
      <defs>
        <linearGradient id="portraitTone" x1="0" y1="0" x2="1" y2="1">
          <stop offset="0" stop-color="var(--photo-light)"/>
          <stop offset="0.55" stop-color="var(--photo-mid)"/>
          <stop offset="1" stop-color="var(--photo-dark)"/>
        </linearGradient>
      </defs>
      <polygon points="0,0 393,0 512,291 408,585 0,585" fill="var(--green-bright)"/>
      <polygon role="img" aria-label="Portrait photo of the personal trainer smiling, wearing a lime green polo shirt" points="0,0 380,0 500,291 396,585 0,585" fill="url(#portraitTone)"/>
    </svg>

    <h1>
      <span class="title title-personal">PERSONAL</span>
      <span class="title title-trainer">TRAINER</span>
      <span class="title title-name">KOFI ADJEI</span>
    </h1>

    <h2 class="section-heading help-heading">How I can help you?</h2>
    <ul class="help-list">
      <li><svg viewBox="0 0 22 14"><path d="M0 4.5h12V0l10 7-10 7V9.5H0z" fill="var(--green-bright)"/></svg>Reduce body fat &nbsp;and increase body definition</li>
      <li><svg viewBox="0 0 22 14"><path d="M0 4.5h12V0l10 7-10 7V9.5H0z" fill="var(--green-bright)"/></svg>Increase stamina, improve agility and speed</li>
      <li><svg viewBox="0 0 22 14"><path d="M0 4.5h12V0l10 7-10 7V9.5H0z" fill="var(--green-bright)"/></svg>Increase strength and size</li>
      <li><svg viewBox="0 0 22 14"><path d="M0 4.5h12V0l10 7-10 7V9.5H0z" fill="var(--green-bright)"/></svg>Plyometric training and conditioning</li>
      <li><svg viewBox="0 0 22 14"><path d="M0 4.5h12V0l10 7-10 7V9.5H0z" fill="var(--green-bright)"/></svg>Flexibility and core strength</li>
    </ul>

    <h2 class="section-heading reviews-heading">What my clients say about me?</h2>
    <p class="testimonial">&nbsp;"With Kofi my training is always challenging and fun. I don’t remember a session to be boring or repetitive. In short time I improved my core strength and flexibility. I can run 10k without stopping. It is amazing improvement. &nbsp;" Laura Whitcombe</p>

    <section class="qualifications-band">
      <h2 class="qualifications-heading">Qualifications</h2>
      <ul class="qualifications-list">
        <li>Advanced Circuit Training</li>
        <li>Advanced Diploma in Personal Training - Level 3 FPRS Registered</li>
        <li>Fitness Instructor - Level 2 FPRS Registered</li>
        <li>Also qualified in – Suspension training, Studio Cycling, Sports Nutrition, Weight Management</li>
      </ul>
      <div class="brand-mark">
        <span class="brand-square"></span>
        <span class="brand-name">Brackmoor Wellness</span>
      </div>
    </section>
  </main>
</body>
</html>
```